TealFathom.com Website design needed!!

We are looking for a website layout to match the attached logo. We specialize in Dive Charters and currently are located in the Virgin Islands off of St. Thomas. Please create a design that is compatible with Bootstrap and have the grid in mind. WE are looking for creative and extremely professional layout design.

Target Market(s)

Scuba Diving, Divers looking for a diving charter in the Virgin Islands.

Number of Pages Required

3 page

Font styles to use
Serif

Requirements
Must have
• Must be Bootstrap friendly.
• Must work with the logo we provided. Colors etc.

```html
<!DOCTYPE html>
<html lang="en">
<head>
<meta charset="utf-8">
<title>Teal Fathom — Dive Charters</title>
<link rel="stylesheet" href="https://fonts.googleapis.com/css2?family=Roboto:ital,wght@0,400;0,500;0,700;1,400&family=Kaushan+Script&display=swap">
<style>
:root{
  --red:#e3202a;
  --orange:#e8830f;
  --blue:#2a8ed1;
  --cyan:#3ccfe2;
  --ink:#333;
  --muted:#666;
  --grey:#e6e6e6;
  --grey-dark:#cfcfcf;
  --deep:#06242e;
  --deeper:#031419;
  --white:#fff;
}
*{box-sizing:border-box;margin:0;padding:0}
html,body{width:1200px;height:2528px;overflow:hidden}
body{font-family:"Roboto",Arial,sans-serif;color:var(--ink);position:relative;background:var(--deeper)}
.page-backdrop{position:absolute;inset:0;background:radial-gradient(ellipse at 50% 25%,#1f5866 0%,#0b3440 40%,#041a20 80%)}
.abs{position:absolute}

/* header */
.site-header{left:74px;top:0;width:1052px;height:202px;background:var(--white);border-bottom:5px solid var(--red)}
.brand{left:22px;top:40px;display:flex;align-items:center;gap:12px}
.brand-dot{width:40px;height:40px;border-radius:50%;background:var(--red)}
.brand-name{font-size:34px;font-weight:700;color:var(--red)}
.social{left:652px;top:20px;display:flex;gap:6px}
.social span{width:34px;height:34px;border:2px solid #777;border-radius:50%}
.call-box{left:782px;top:0;width:262px;height:78px;background:var(--red);color:var(--white);text-align:center;padding-top:10px}
.call-box .phone{font-size:30px;font-weight:500}
.call-box .mail{font-size:14px}
.main-nav{left:22px;top:162px;display:flex;gap:64px;font-size:16px;font-weight:500;color:#444}
.search-icon{left:1006px;top:160px}

/* hero */
.hero{left:0;top:202px;width:1200px;height:553px;background:linear-gradient(180deg,#0d4050 0%,#1a6070 40%,#082a33 100%)}
.hero-caption{left:80px;top:525px;font-family:"Kaushan Script",cursive;font-size:52px;color:var(--white)}
.slider-controls{left:74px;top:712px;display:flex;gap:6px}
.slider-controls span{width:26px;height:26px;border:2px solid var(--white);display:flex;align-items:center;justify-content:center}
.charter-search{left:698px;top:320px;width:411px;height:362px;background:var(--grey);padding:80px 26px 0}
.charter-search .banner{left:-18px;top:-50px;width:440px;height:92px;background:var(--red);color:var(--white);font-size:25px;padding:18px 26px;line-height:1.15}
.charter-search label{display:flex;align-items:center;gap:10px;font-size:14px;color:#555;margin-bottom:12px}
.charter-search label i{width:14px;height:14px;border-radius:50%;background:var(--white);border:1px solid #bbb}
.field{height:42px;background:var(--white);border-radius:4px;margin-bottom:14px;font-size:14px;color:#777;padding:13px 14px}
.btn-find{height:56px;background:var(--orange);color:var(--white);font-size:22px;font-weight:700;text-align:center;padding-top:15px;border-radius:3px}

/* about */
.about{left:74px;top:755px;width:1052px;height:290px;background:var(--white);border-top:5px solid var(--red);text-align:center;padding:48px 36px 0}
.about h1{font-size:26px;font-weight:500;color:var(--blue);margin-bottom:20px}
.about p{font-size:14px;line-height:24px;color:#444}
.more-link{display:inline-flex;align-items:center;gap:8px;font-size:12px;margin-top:24px}
.ring{width:20px;height:20px;border:2px solid var(--red);border-radius:50%;display:inline-flex;align-items:center;justify-content:center;color:var(--red);font-size:11px}

/* news */
.news{left:74px;top:1045px;width:539px;height:345px;background:var(--grey)}
.tabs{display:flex;height:58px;background:var(--grey-dark);padding:12px 0 0 14px;gap:4px}
.tabs span{padding:10px 16px;font-size:16px}
.tabs .active{background:var(--grey)}
.tabs .idle{background:#d9d9d9;color:#777}
.news-item{display:flex;gap:16px;padding:16px 18px 0}
.thumb{width:96px;height:94px;background:linear-gradient(135deg,#2a7ac0,#0f3c70)}
.news-item h3{font-size:16px;font-weight:700;margin:6px 0 4px}
.news-item .date{font-size:11px;color:var(--muted);margin-bottom:8px}
.news-item p{font-size:13px;line-height:20px;color:#555}
.panel-foot{left:0;bottom:0;width:100%;height:40px;border-top:1px solid #ccc;display:flex;align-items:center;gap:8px;padding-left:26px;font-size:12px;color:#444}
.video{left:613px;top:1045px;width:513px;height:345px;background:radial-gradient(circle at 50% 10%,#3ab4e0,#0d4f8e 55%,#06264a)}
.play{left:215px;top:112px;width:90px;height:90px;border:5px solid var(--white);border-radius:50%}
.video .panel-foot{background:rgba(0,0,0,.35);border:none;color:#aaa}

/* feedback */
.feedback{left:74px;top:1390px;width:1052px;height:396px;background:linear-gradient(180deg,#1e6a88,#0b3246);color:var(--white);text-align:center;padding-top:50px}
.feedback h2{font-size:24px;font-weight:500}
.feedback .sub{font-size:13px;font-weight:500;margin-bottom:24px}
.feedback blockquote{width:660px;margin:0 auto;font-style:italic;font-size:14px;line-height:24px}
.quote-mark{font-size:52px;font-weight:700;top:110px}
.feedback .name{font-size:15px;font-weight:700;margin-top:24px}
.feedback .role{font-size:12px}
.dots{left:490px;top:340px;display:flex;gap:5px;align-items:center}
.dots i{width:7px;height:7px;border-radius:50%;background:var(--white)}
.dots i.on{width:12px;height:12px}

/* newsletter */
.newsletter{left:74px;top:1786px;width:1052px;height:189px;background:var(--cyan);text-align:center;padding-top:34px}
.newsletter h2{font-size:26px;font-weight:500;color:var(--white);margin-bottom:20px}
.news-form{display:flex;gap:18px;justify-content:center}
.news-form .input{width:312px;height:42px;background:var(--white);border-radius:3px;text-align:left;padding:13px 16px;font-size:14px;color:#777}
.news-form .subscribe{width:192px;height:42px;border:2px solid var(--white);border-radius:3px;color:var(--white);font-size:14px;padding-top:11px}
.newsletter .opt-out{font-style:italic;font-size:13px;color:#2d8a99;margin-top:14px}

/* footer */
.footer-nav{left:0;top:2037px;width:1200px;display:flex;justify-content:center;gap:46px;color:var(--white);font-size:14px;font-weight:500}
.contact-row{left:165px;top:2104px;width:820px;display:flex;justify-content:space-between}
.contact{display:flex;gap:16px;color:var(--white);font-size:14px;line-height:24px;width:260px;border-bottom:1px solid rgba(255,255,255,.2);padding-bottom:12px}
.contact .ic{width:28px;height:28px;border:2px solid var(--white);border-radius:50%;flex:none}
.footer-brand{left:0;top:2270px;width:1200px;display:flex;justify-content:center;align-items:center;gap:18px}
.footer-brand .brand-dot{width:64px;height:64px}
.footer-brand .brand-name{font-size:62px}
.copyright{left:0;top:2428px;width:1200px;display:flex;justify-content:center;align-items:center;gap:14px;color:var(--white);font-size:14px}
.copyright .social span{border-color:var(--white)}
</style>
</head>
<body>
<div class="page-backdrop" role="img" aria-label="Dark underwater photograph of a school of fish filling the background"></div>

<header class="site-header abs">
  <div class="brand abs"><span class="brand-dot"></span><span class="brand-name">Teal Fathom</span></div>
  <div class="social abs"><span></span><span></span><span></span></div>
  <div class="call-box abs"><div class="phone">(555)-018-2736</div><div class="mail">info@tealfathom.com</div></div>
  <nav class="main-nav abs"><span>TEAL FATHOM</span><span>ABOUT US</span><span>CONTACT</span><span>LEARN MORE</span><span>SCHEDULE</span></nav>
  <svg class="search-icon abs" width="22" height="22" viewBox="0 0 22 22"><circle cx="9" cy="9" r="6.5" fill="none" stroke="#aaa" stroke-width="3"/><line x1="14" y1="14" x2="20" y2="20" stroke="#aaa" stroke-width="3"/></svg>
</header>

<section class="hero abs" role="img" aria-label="Diver in a red wetsuit swimming through a dense school of silver fish"></section>
<div class="hero-caption abs">Lorem ipsum dolor sit amet</div>
<div class="slider-controls abs">
  <span><svg width="10" height="12"><polygon points="9,1 1,6 9,11" fill="none" stroke="#fff" stroke-width="1.5"/></svg></span>
  <span><svg width="10" height="12"><polygon points="1,1 9,6 1,11" fill="none" stroke="#fff" stroke-width="1.5"/></svg></span>
</div>

<form class="charter-search abs">
  <div class="banner abs">Search for your<br><b>dream charter TODAY!</b></div>
  <label><i></i>I have approximate dates</label>
  <label><i></i>I'm flexible</label>
  <div class="field">First Name</div>
  <div class="field">Email</div>
  <div class="btn-find">FIND CHARTERS</div>
</form>

<section class="about abs">
  <h1>TEAL FATHOM CHARTERS AND SCUBA</h1>
  <p>Lorem ipsum dolor sit amet, consectetur adipiscing elit. Fusce semper vitae leo sit amet vehicula. Sed viverra, justo ac consectetur hendrerit, lacus elit tempor urna, gravida mattis lacus ex sed sem. Nam consectetur, arcu in iaculis dapibus, urna felis congue elit, in consectetur nisi massa sed metus. Nullam a tortor ut mauris auctor interdum id vel neque. In commodo diam at faucibus dictum. Nulla condimentum elit a odio consectetur, vel eleifend libero sagittis. Praesent sed erat a ante laoreet dapibus et ultrices sem. Vivamus elit lectus, ullamcorper et vestibulum eget</p>
  <div class="more-link"><span class="ring">›</span>MORE</div>
</section>

<section class="news abs">
  <div class="tabs"><span class="active">News</span><span class="idle">Events</span></div>
  <article class="news-item"><div class="thumb" role="img" aria-label="Two divers underwater"></div><div><h3>This is a test Title</h3><div class="date">18 JAN 2016</div><p>Lorem ipsum dolor sit amet, consectetur adipiscing elit.<br>Fusce semper vitae leo sit amet vehicula.</p></div></article>
  <article class="news-item"><div class="thumb" role="img" aria-label="Guests aboard a dive boat"></div><div><h3>This is a test Title</h3><div class="date">18 JAN 2016</div><p>Lorem ipsum dolor sit amet, consectetur adipiscing elit.<br>Fusce semper vitae leo sit amet vehicula.</p></div></article>
  <div class="panel-foot abs"><span class="ring">›</span>VIEW MORE NEWS</div>
</section>

<section class="video abs" role="img" aria-label="Video still of a diver silhouetted against sunlit blue water">
  <svg class="play abs" viewBox="0 0 90 90"><polygon points="34,24 66,45 34,66" fill="#fff"/></svg>
  <div class="panel-foot abs"><span class="ring">›</span>VIEW MORE VIDEOS</div>
</section>

<section class="feedback abs" role="img" aria-label="Silhouettes of divers in deep blue water behind the guest testimonial">
  <h2>GUEST FEEDBACK</h2>
  <div class="sub">WHAT OUR GUESTS THINK OF US</div>
  <span class="quote-mark abs" style="left:140px">“</span>
  <span class="quote-mark abs" style="right:140px">”</span>
  <blockquote>Lorem ipsum dolor sit amet, consectetur adipiscing elit. Fusce semper vitae leo sit amet vehicula. Sed viverra, justo ac consectetur hendrerit, lacus elit tempor urna, gravida mattis lacus ex sed sem. Nam consectetur, arcu in iaculis dapibus, urna felis congue elit, in consectetur nisi massa sed metus. Nullam a tortor ut mauris auctor interdum id vel neque. In commodo diam at faucibus dictum. Nulla condimentum elit a odio consectetur, vel eleifend libero sagittis.</blockquote>
  <div class="name">JOHN DOE</div>
  <div class="role">Lorem ipsum dolor</div>
  <div class="dots abs"><i class="on"></i><i></i><i></i><i></i><i></i><i></i></div>
</section>

<section class="newsletter abs">
  <h2>JOIN OUR NEWSLETTER</h2>
  <div class="news-form"><div class="input">Your name</div><div class="input">Your email</div><div class="subscribe">SUBSCRIBE</div></div>
  <p class="opt-out">If you like to stop receiving our newsletter, please click here</p>
</section>

<nav class="footer-nav abs"><span>TEAL FATHOM</span><span>ABOUT US</span><span>CONTACT</span><span>LEARN MORE</span><span>SCHEDULE</span></nav>

<div class="contact-row abs">
  <div class="contact"><svg class="ic" viewBox="0 0 28 28"><path d="M14 7a5 5 0 0 0-5 5c0 4 5 9 5 9s5-5 5-9a5 5 0 0 0-5-5z" fill="#fff"/></svg><div>Your Company LTD.<br>Street Name, 000000<br>City Name</div></div>
  <div class="contact"><svg class="ic" viewBox="0 0 28 28"><path d="M9 8c2 0 3 3 2 4s2 4 4 5c1-1 4 0 4 2s-3 3-6 1-7-6-7-9 1-3 3-3z" fill="#fff"/></svg><div>Phone<br>1-000-000-0000</div></div>
  <div class="contact"><svg class="ic" viewBox="0 0 28 28"><rect x="7" y="9" width="14" height="10" fill="none" stroke="#fff" stroke-width="1.6"/><polyline points="7,9 14,15 21,9" fill="none" stroke="#fff" stroke-width="1.6"/></svg><div>Email<br>info@yourdomain.com</div></div>
</div>

<div class="footer-brand abs"><span class="brand-dot"></span><span class="brand-name">Teal Fathom</span></div>

<footer class="copyright abs"><span>© 2016 Teal Fathom. All Rights Reserved</span><div class="social" style="display:flex;gap:6px"><span style="width:32px;height:32px;border:2px solid #fff;border-radius:50%"></span><span style="width:32px;height:32px;border:2px solid #fff;border-radius:50%"></span><span style="width:32px;height:32px;border:2px solid #fff;border-radius:50%"></span></div></footer>
</body>
</html>
```